Business Card Design Project

Mabel's Tonics is a natural skincare business and we need a business card designed. The company focuses on natural products and will be launching with body scrubs and bath fizzies and our mission statement is: To deliver high quality natural beauty products at a good value. It's two cards - one design - the only information changing would be name and email address

Target Market(s)

Females ages 20-50

Industry/Entity Type

Business

Requirements
Must have
• Mabel's Tonics

Corinne Halvorsen-Pitt
T: 800-417-9368
E: Corinne@MabelsTonics.example
W: www.MabelsTonics.example

Ulrich Benedetti
T: 800-417-9368
E: Ulrich@MabelsTonics.example
W: www.MabelsTonics.example
Nice to have
• I'd like to use the colors or text found at www.mabelstonics.example but I'm open to suggestions since design isn't set in stone yet. I would also like to have the words .....a little bit of magic somewhere under the company name in a different type of font. I would like a design that feels clean and maybe a retro feel to it - front and back would be nice but not mandatory

```html
<!DOCTYPE html>
<html lang="en">
<head>
<meta charset="utf-8">
<title>Mabel's Tonics — Business Cards</title>
<link rel="stylesheet" href="https://fonts.googleapis.com/css2?family=Source+Sans+3:wght@400;500&display=swap">
<style>
  :root {
    --brand-blue: #2399c8;
    --brand-purple: #7b2a8a;
    --card-white: #ffffff;
    --backdrop: #eeeae5;
    --card-edge: #d9d4ce;
    --text-font: "Source Sans 3", Arial, sans-serif;
  }
  * { margin: 0; padding: 0; box-sizing: border-box; }
  html, body { width: 1200px; height: 1000px; overflow: hidden; }
  body { background: var(--backdrop); position: relative; font-family: var(--text-font); }

  .card { position: absolute; width: 525px; height: 302px; }
  .card--front { background: var(--brand-blue); }
  .card--back { background: var(--card-white); border: 1px solid var(--card-edge); }

  .card--front-left  { left: 57px;  top: 40px; }
  .card--back-left   { left: 57px;  top: 384px; }
  .card--front-right { left: 627px; top: 321px; }
  .card--back-right  { left: 627px; top: 659px; }

  .brand-name {
    position: absolute; display: flex; align-items: center; gap: 12px;
    font-family: var(--text-font); font-weight: 400; line-height: 1; white-space: nowrap;
  }
  .brand-name__mark { width: 14px; height: 14px; border-radius: 50%; background: currentColor; flex: none; }

  .tagline {
    position: absolute; font-family: var(--text-font); font-weight: 400;
    line-height: 1; letter-spacing: 0.08em; text-transform: uppercase; white-space: nowrap;
  }

  .card--front .brand-name {
    left: 0; right: 0; top: 118px; justify-content: center;
    color: var(--card-white); font-size: 40px;
  }
  .card--front .tagline {
    left: 0; right: 0; bottom: 26px; text-align: center;
    color: var(--card-white); font-size: 13px;
  }

  .card--back .brand-name {
    right: 30px; top: 222px; color: var(--brand-purple); font-size: 32px;
  }
  .card--back .brand-name__mark { width: 12px; height: 12px; }
  .card--back .tagline {
    left: 43px; top: 234px; color: var(--brand-blue); font-size: 12px;
  }

  .holder-name {
    position: absolute; left: 33px; top: 22px;
    color: var(--brand-blue); font-size: 29px; font-weight: 500; line-height: 1;
  }
  .contact-list { position: absolute; left: 43px; top: 98px; list-style: none; }
  .contact-list li { font-size: 19.5px; line-height: 26.5px; color: var(--brand-purple); }
  .contact-list .contact-label { color: var(--brand-blue); }
</style>
</head>
<body>

  <section class="card card--front card--front-left">
    <div class="brand-name"><span class="brand-name__mark"></span>Mabel's Tonics</div>
    <p class="tagline">a little bit of magic</p>
  </section>

  <section class="card card--back card--back-left">
    <h2 class="holder-name">Corinne Halvorsen-Pitt</h2>
    <ul class="contact-list">
      <li><span class="contact-label">T:</span> 800-417-9368</li>
      <li><span class="contact-label">E:</span> Corinne@MabelsTonics.example</li>
      <li><span class="contact-label">W:</span> www.MabelsTonics.example</li>
    </ul>
    <p class="tagline">a little bit of magic</p>
    <div class="brand-name"><span class="brand-name__mark"></span>Mabel's Tonics</div>
  </section>

  <section class="card card--front card--front-right">
    <div class="brand-name"><span class="brand-name__mark"></span>Mabel's Tonics</div>
    <p class="tagline">a little bit of magic</p>
  </section>

  <section class="card card--back card--back-right">
    <h2 class="holder-name">Ulrich Benedetti</h2>
    <ul class="contact-list">
      <li><span class="contact-label">T:</span> 800-417-9368</li>
      <li><span class="contact-label">E:</span> Ulrich@MabelsTonics.example</li>
      <li><span class="contact-label">W:</span> www.MabelsTonics.example</li>
    </ul>
    <p class="tagline">a little bit of magic</p>
    <div class="brand-name"><span class="brand-name__mark"></span>Mabel's Tonics</div>
  </section>

</body>
</html>
```